Bright Harbor Capital website

Build a website template for the Bright Harbor Capital fund.
Looking for a cool website design showing companies we are using the latest in web design trends. We want to attract app developers, typically the younger set.
A good example of one of our competitive firms is http://tallmeadowfund.example
The required components for the website include:
1) Funding application
2) about our firm
a) Partner profiles - We will include photographs and bios about each of the partners in our firm.
b) Invest with Bright Harbor - This will include information how to invest with our fund
c) our process - About our process for evaluating, funding and helping build successful businesses - This will include a narrative about the target companies, how we work, the type of deals we are interested in, our expectations, etc ...
3) Investment profiles - Stories about the companies we invest with
4) News - Output from our twitter feed and copies of our Blog posts

```html
<!DOCTYPE html>
<html lang="en">
<head>
<meta charset="utf-8">
<title>Bright Harbor Capital</title>
<link href="https://fonts.googleapis.com/css2?family=Lato:ital,wght@0,400;0,700;1,400&display=swap" rel="stylesheet">
<style>
:root{
  --green:#5f9f13;
  --green-dark:#4e8a0c;
  --green-light:#7ab93a;
  --ink:#1f1f1f;
  --grey-text:#555;
  --nav-bg:#e5e5e5;
  --border:#d8d8d8;
  --white:#fff;
}
*{box-sizing:border-box;margin:0;padding:0}
html,body{width:1200px;height:910px;overflow:hidden;background:var(--white);font-family:'Lato',sans-serif;color:var(--ink)}
.page{position:relative;width:1200px;height:910px}
.utility-bar{position:absolute;top:0;left:0;width:100%;height:19px;background:var(--green)}
.utility-links{position:absolute;right:250px;top:5px;display:flex;gap:8px;font-size:7.5px;color:var(--white)}
.utility-links a{color:var(--white);text-decoration:none}
.utility-links a.active{text-decoration:underline}
.brand{position:absolute;left:250px;top:44px;display:flex;align-items:center;gap:8px}
.brand-dot{width:30px;height:30px;border-radius:50%;background:var(--green)}
.brand-name{font-size:23px;font-weight:700;color:var(--green)}
.main-nav{position:absolute;top:98px;left:0;width:100%;height:22px;background:var(--nav-bg)}
.main-nav ul{position:absolute;left:254px;width:692px;top:4px;display:flex;justify-content:space-between;list-style:none;font-size:12px;color:var(--grey-text)}
.main-nav li.current{color:var(--green);text-decoration:underline}
.funding-cta{position:absolute;left:250px;top:134px;width:194px;height:141px;border:1px solid var(--green-dark);background:linear-gradient(165deg,var(--green) 0%,var(--green) 55%,var(--green-light) 56%,#88c24a 100%);text-align:center}
.funding-cta h2{margin-top:20px;font-size:31px;line-height:32px;font-weight:700;color:var(--white);letter-spacing:.5px}
.funding-cta p{font-size:20.5px;font-weight:700;color:#1e2a10;line-height:22px}
.funding-cta svg{position:absolute;left:82px;top:89px}
.panel{position:absolute;left:250px;width:193px;background:var(--white);border:1px solid var(--border);box-shadow:0 6px 6px -5px rgba(0,0,0,.35)}
.panel-head{position:relative;height:30px;background:var(--green);color:var(--white);font-size:13px;padding:9px 0 0 14px}
.panel-head::after{content:"";position:absolute;left:12px;bottom:-7px;border-left:7px solid transparent;border-right:7px solid transparent;border-top:7px solid var(--green)}
.view-all{position:absolute;right:13px;font-size:10px;color:var(--green);text-decoration:underline}
.profiles{top:301px;height:231px}
.partner-list{list-style:none;margin-top:20px;text-align:center}
.partner-list li{height:47px;display:flex;align-items:center;justify-content:center;gap:6px;font-size:15px;font-weight:700;color:#1d3f7a}
.partner-list li.bank{color:#333;font-weight:400;font-size:16px}
.partner-list li.marsh{color:#1d4a2a}
.partner-mark{width:10px;height:10px;background:currentColor}
.profiles .view-all{top:212px}
.news{top:560px;height:246px}
.news-list{list-style:none;margin:14px 0 0 26px}
.news-list li{position:relative;height:43.6px;font-size:9.5px}
.news-list li::before{content:"";position:absolute;left:-9px;top:5px;width:3px;height:3px;border-radius:50%;background:var(--green)}
.news-date{display:block;color:var(--green);margin-bottom:3px}
.news .view-all{top:225px}
.hero-photo{position:absolute;left:474px;top:134px;width:476px;height:240px;border:1px solid var(--border);background:linear-gradient(100deg,#cfd6dc 0%,#eef1f3 40%,#9aa3ab 70%,#dfe4e6 100%)}
.divider{position:absolute;left:474px;top:389px;width:476px;height:1px;background:var(--border)}
.card{position:absolute;background:var(--white);border:1px solid var(--border);box-shadow:0 7px 7px -6px rgba(0,0,0,.4);padding:12px 13px;font-size:12.8px;line-height:17.2px}
.card h3{font-size:13.6px;font-weight:400;color:var(--green);line-height:16px;margin-bottom:1px}
.about{left:474px;top:404px;width:476px;height:179px}
.about ul{list-style:none}
.about li{position:relative;padding-left:10px}
.about li::before{content:"";position:absolute;left:1px;top:7px;width:4px;height:4px;border-radius:50%;background:var(--ink)}
.growing{left:474px;top:611px;width:214px;height:195px}
.quote{left:725px;top:611px;width:224px;height:195px;font-style:italic;padding-top:14px}
.site-footer{position:absolute;left:0;top:836px;width:100%;height:74px;background:var(--green);color:var(--white);font-family:Arial,sans-serif;font-size:9px}
.site-footer .copy{position:absolute;left:250px;top:12px}
.site-footer .credit{position:absolute;right:250px;top:12px}
</style>
</head>
<body>
<div class="page">
  <div class="utility-bar">
    <nav class="utility-links"><a class="active">MEMBERS</a><a>SPONSORS</a><a>LATEST NEWS</a></nav>
  </div>

  <header class="brand">
    <span class="brand-dot"></span>
    <span class="brand-name">Bright Harbor Capital</span>
  </header>

  <nav class="main-nav">
    <ul>
      <li class="current">HOME</li><li>ABOUT US</li><li>PARTNERS PROFILE</li><li>INVEST</li><li>OUR PROCESS</li><li>NEWS</li><li>INVESTMENT PROFILES</li><li>CONTACT US</li>
    </ul>
  </nav>

  <a class="funding-cta">
    <h2>FUNDING</h2>
    <p>APPLICATION</p>
    <svg width="30" height="30" viewBox="0 0 30 30" aria-hidden="true">
      <circle cx="15" cy="15" r="14" fill="#fff" stroke="#3d6e0a" stroke-width="1.5"/>
      <path d="M12 8 L20 15 L12 22 Z" fill="#1a1a1a"/>
    </svg>
  </a>

  <section class="panel profiles">
    <div class="panel-head">INVESTMENT PROFILES</div>
    <ul class="partner-list">
      <li><span class="partner-mark"></span>Linden Pryce &amp; Vale</li>
      <li class="bank">The Bank of Eastmoor</li>
      <li class="marsh"><span class="partner-mark"></span>Marsh &amp; Tolliver</li>
    </ul>
    <a class="view-all">VIEW ALL</a>
  </section>

  <section class="panel news">
    <div class="panel-head">LATEST NEWS</div>
    <ul class="news-list">
      <li><span class="news-date">01/15/14</span>Lorem Ipsum is simply dummy text</li>
      <li><span class="news-date">01/15/14</span>Lorem Ipsum is simply dummy text</li>
      <li><span class="news-date">01/15/14</span>Lorem Ipsum is simply dummy text</li>
      <li><span class="news-date">01/15/14</span>Lorem Ipsum is simply dummy text</li>
    </ul>
    <a class="view-all">VIEW ALL</a>
  </section>

  <div class="hero-photo" role="img" aria-label="Photo of two business partners in suits reviewing a folder outdoors"></div>
  <div class="divider"></div>

  <section class="card about">
    <h3>ABOUT OUR FIRM</h3>
    <ul>
      <li>Partner profiles - We will include photographs and bios about each of the partners in our firm.</li>
      <li>Invest with Bright Harbor - This will include information how to invest with our fund</li>
      <li>our process - About our process for evaluating, funding and helping build successful businesses - This will include a narrative about the target companies, how we work, the type of deals we are interested in, our expectations, etc</li>
    </ul>
  </section>

  <section class="card growing">
    <h3>GROWING BUSINESSES</h3>
    <p>Lorem Ipsum is simply dummy text of the printing and typesetting industry. Lorem Ipsum has been the industry's standard dummy text ever since the 1500s, when an unknown printer took a galley of type and scrambled it to make a type specimen book.</p>
  </section>

  <section class="card quote">
    <p>Lorem Ipsum is simply dummy text of the printing and typesetting industry. Lorem Ipsum has been the industry's standard dummy text ever since the 1500s, when an unknown printer took a galley of type and scrambled it to make a type specimen book..............</p>
  </section>

  <footer class="site-footer">
    <span class="copy">© Copyright Bright Harbor Capital 2014 - All rights reserved.</span>
    <span class="credit">Website Designed by Signal Pier Studio.</span>
  </footer>
</div>
</body>
</html>
```